Corvane

I'm looking for business cards with the logo I've attached. I don't have an specific idea in mind and open to anything. All the usual info will be involved. Name, position in company, nr, email, address

```html
<!DOCTYPE html>
<html lang="en">
<head>
<meta charset="utf-8">
<title>Corvane Designs – Business Cards</title>
<link href="https://fonts.googleapis.com/css2?family=Montserrat:wght@400;500;600;700&display=swap" rel="stylesheet">
<style>
  :root {
    --navy: #1b2f4f;
    --gold: #eeb133;
    --white: #ffffff;
    --stage: #3a3a3c;
    --ink: #1b2f4f;
  }
  * { box-sizing: border-box; margin: 0; padding: 0; }
  html, body {
    width: 1200px; height: 1200px; overflow: hidden;
    background: var(--stage);
    font-family: "Montserrat", sans-serif;
  }
  .sheet {
    width: 1200px; height: 1200px;
    display: flex; flex-direction: column;
    align-items: center; justify-content: center; gap: 56px;
  }
  .card {
    position: relative;
    width: 900px; height: 514px;
    border-radius: 28px;
    overflow: hidden;
  }
  .card--back {
    background: var(--navy);
    display: flex; align-items: center; justify-content: center;
  }
  .card--front { background: var(--white); }

  .wordmark { text-align: center; color: var(--gold); font-weight: 600; }
  .wordmark__name { display: block; font-size: 88px; line-height: 1; letter-spacing: 1px; }
  .wordmark__sub { display: block; font-size: 34px; letter-spacing: 22px; margin-top: 14px; padding-left: 22px; }
  .wordmark__dot {
    width: 26px; height: 26px; border-radius: 50%;
    background: var(--gold); margin: 0 auto 26px;
  }

  .card--front .wordmark {
    position: absolute; right: 70px; top: 70px;
  }
  .card--front .wordmark__name { font-size: 64px; }
  .card--front .wordmark__sub { font-size: 25px; letter-spacing: 16px; padding-left: 16px; margin-top: 10px; }
  .card--front .wordmark__dot { width: 20px; height: 20px; margin-bottom: 18px; }

  .holder { position: absolute; left: 70px; top: 230px; color: var(--ink); }
  .holder__name { font-size: 30px; font-weight: 700; letter-spacing: 0.5px; }
  .holder__role { font-size: 20px; font-weight: 600; color: var(--gold); margin-top: 4px; }
  .holder__rule { width: 56px; height: 3px; background: var(--gold); margin: 14px 0 22px; }
  .holder__address, .holder__email { font-size: 19px; line-height: 1.4; font-weight: 500; }
  .holder__email { display: flex; align-items: center; gap: 10px; margin-top: 2px; }

  .contacts { position: absolute; left: 520px; bottom: 60px; color: var(--ink); }
  .contacts__row { display: flex; align-items: center; gap: 12px; font-size: 21px; font-weight: 500; line-height: 1.5; }
  .contacts__row strong { font-weight: 700; }
  .icon { width: 18px; height: 18px; flex: none; }
</style>
</head>
<body>
<main class="sheet">
  <section class="card card--back">
    <div class="wordmark">
      <div class="wordmark__dot"></div>
      <span class="wordmark__name">CORVANE</span>
      <span class="wordmark__sub">DESIGNS</span>
    </div>
  </section>

  <section class="card card--front">
    <div class="holder">
      <h1 class="holder__name">DANIEL HARTLEY</h1>
      <p class="holder__role">Owner</p>
      <div class="holder__rule"></div>
      <p class="holder__address">14/08 Bramley Street,<br>Oak Ridge, Vic 4150, Graz, Austria</p>
      <p class="holder__email">
        <svg class="icon" viewBox="0 0 20 20"><rect x="2" y="5" width="16" height="11" fill="none" stroke="#eeb133" stroke-width="2"/><path d="M2 5l8 6 8-6" fill="none" stroke="#eeb133" stroke-width="2"/></svg>
        info@corvanedesigns.com
      </p>
    </div>

    <div class="wordmark">
      <div class="wordmark__dot"></div>
      <span class="wordmark__name">CORVANE</span>
      <span class="wordmark__sub">DESIGNS</span>
    </div>

    <div class="contacts">
      <p class="contacts__row">
        <svg class="icon" viewBox="0 0 20 20"><path d="M5 2l3 4-2 2c1 2 3 4 5 5l2-2 4 3-2 3C9 17 3 11 2 4z" fill="#eeb133"/></svg>
        (555) 210 4471
      </p>
      <p class="contacts__row">
        <svg class="icon" viewBox="0 0 20 20"><rect x="6" y="2" width="9" height="16" rx="2" fill="none" stroke="#eeb133" stroke-width="1.8"/></svg>
        (555) 210 4472
      </p>
      <p class="contacts__row">
        <svg class="icon" viewBox="0 0 20 20"><circle cx="10" cy="10" r="8" fill="none" stroke="#eeb133" stroke-width="1.8"/><path d="M2 10h16M10 2c-3 3-3 13 0 16M10 2c3 3 3 13 0 16" fill="none" stroke="#eeb133" stroke-width="1.5"/></svg>
        <span>www.<strong>corvanedesigns</strong>.com</span>
      </p>
    </div>
  </section>
</main>
</body>
</html>
```